Ned Halvorsen Executive Coach Business Card Design

I need a new card design for my Executive Coaching practice. I am a Clinical Psychotherapist and Executive Coach. I help my clients get the most out of life by developing their personal and professional skills and abilities.

I work with senior executives. My design needs to be high end. I am thinking gloss on the front. I am also thinking contemporary. I am going to use a black, grey and red colour scheme on the the website. I am thinking grey with black and red accents. I would also like a water mark included on the card.

Target Market(s)

Senior Executives In major Companies

Industry/Entity Type

Business

Contact Information for Business Card

On the front

Ned Halvorsen
Clinical Psychotherapist and Executive Coach
For Personal and Professional Success

On the Back

Tarrant office
87 Tarrant Vale Road Tarrant

North Sydney Office
Suite 309 / 41 Pellow Street North Sydney

Danforth Street Office
Suite 512 / 248 Danforth Street Sydney CBD

Phone 02 95517384
Email ned@nedhalvorsen.example.au

Requirements
Must have
• Friendly but professional
Water Mark
Gloss Front

```html
<!DOCTYPE html>
<html lang="en">
<head>
<meta charset="utf-8">
<title>Ned Halvorsen – Business Card Back</title>
<link rel="stylesheet" href="https://fonts.googleapis.com/css2?family=Cormorant+Garamond:ital,wght@0,600;1,600&display=swap">
<style>
  :root {
    --grey-light: #8c8f91;
    --grey-mid: #5f6264;
    --grey-dark: #2c2f31;
    --ink: #f3f3f2;
    --accent-red: #c60c0c;
    --edge-dark: #1e2022;
    --watermark: rgba(200, 203, 205, 0.22);
  }
  html, body {
    margin: 0;
    padding: 0;
    width: 1200px;
    height: 726px;
    overflow: hidden;
    background: #ffffff;
  }
  .card-back {
    position: relative;
    width: 1200px;
    height: 726px;
    overflow: hidden;
    background: radial-gradient(ellipse 62% 70% at 55% 45%, var(--grey-light) 0%, var(--grey-mid) 55%, var(--grey-dark) 100%);
    font-family: "Cormorant Garamond", Georgia, serif;
    font-weight: 600;
    font-variant: small-caps;
    color: var(--ink);
  }
  .card-decor {
    position: absolute;
    inset: 0;
    width: 1200px;
    height: 726px;
  }
  .contact-list {
    position: absolute;
    right: 90px;
    top: 0;
    margin: 0;
    text-align: right;
  }
  .contact-line {
    position: absolute;
    right: 0;
    white-space: nowrap;
    font-size: 41px;
    line-height: 1;
    letter-spacing: 0.2px;
  }
  .office-name,
  .contact-label {
    font-style: italic;
  }
</style>
</head>
<body>
  <main class="card-back">
    <svg class="card-decor" viewBox="0 0 1200 726" aria-hidden="false">
      <circle class="watermark-circle" cx="400" cy="380" r="250" fill="none" stroke="var(--watermark)" stroke-width="14" role="img" aria-label="Faint monogram watermark area"></circle>
      <path class="accent-edge" d="M1200 70 Q1140 363 1200 686 Z" fill="var(--edge-dark)"></path>
      <path class="accent-arc" d="M1200 82 Q1150 363 1200 674 Z" fill="var(--accent-red)"></path>
    </svg>

    <address class="contact-list">
      <span class="contact-line office-name" style="top:72px">Tarrant Office</span>
      <span class="contact-line office-address" style="top:128px">87 Tarrant Vale Road Tarrant</span>

      <span class="contact-line office-name" style="top:235px">North Sydney Office</span>
      <span class="contact-line office-address" style="top:290px">Suite 309 / 41 Pellow Street North Sydney</span>

      <span class="contact-line office-name" style="top:397px">Danforth Street Office</span>
      <span class="contact-line office-address" style="top:452px">Suite 512 / 248 Danforth Street Sydney CBD</span>

      <span class="contact-line phone" style="top:560px"><span class="contact-label">Phone</span> 02 95517384</span>
      <span class="contact-line email" style="top:616px"><span class="contact-label">Email</span> ned@nedhalvorsen.example.au</span>
    </address>
  </main>
</body>
</html>
```